complete redesign of VitaPlate.com

VITAPLATE.COM
MAIN MANU

We need it cut into HTML / Wordpress Friendly.... Our developer will handle all the WP / PHP coding, but we need it placed into HTML format so he can put into wordpress.

Please see the old vitaplate.com by visiting www.vitaplate.com... we want something completely different, but... just use this site for reference as to audience, theme, etc... we want something where it is science meets diet in helping fight cancer :)

WE NEED SOMETHING MORE MODERN AND MEDICAL IN TERMS OF DESIGN

See below:

1 CANCER NEWS
2 NUTRITION DIAGNOSTICS
3 DIET STEPS
4 DIET SUPPLEMENTS IN CANCER 
5 DICTIONARY OF MARKINGS ON FOOD
6 FERNAMEAL VIDEOS
7 YOUR INDIVIDUAL DIET - SUBSCRIPTION

a. CANCER NEWS - latest articles relating to cancer prevention research treatments

b. NUTRITION DIAGNOSTICS -  description of the research that must be done to determine the degree of malnutrition of the body a place on the charts
pictures, etc.

c. DIET STEPS 
(sub menu - @)
¥ prevention of oncological - @
¥ diet chemotherapy - @
¥ diet in radiotherapy - @
¥ hormonal diet - @
¥ diet during convalescence - @

d. DIET SUPPLEMENTS IN CANCER - articles describing various supplements summary tables, etc.

e. DICTIONARY OF MARKINGS ON FOOD - composition, translation of labels on food, itd.

f. FERNAMEAL VIDEOS 
(sub menu - @)
¥ healthy cooking - @
¥ meal preparation - @
¥ storage of food - @
¥ eco food - @
¥ rehabilitation - @
¥ yoga - @
¥ exercises - @
¥ psycho-oncology training - @
¥ music therapy - @

g. YOUR INDIVIDUAL DIET -  individual personalized diet for subscribing. We
add this point by developing a system of diet.

After 3 months, we will add special individual programs that mix diet, exercise and psychological lectures

Industry/Entity Type

Medical

Logo Text

Vita Plate / VitaPlate.com

Number of Pages Required

5+ page

Font styles to use
Sans Serif

Colors
ec1f27
9bcb3c
ffffff

Requirements
Must have
• HTML/CSS

```html
<!DOCTYPE html>
<html lang="en">
<head>
<meta charset="utf-8">
<title>Vita Plate – The Science Behind What We Eat</title>
<link rel="stylesheet" href="https://fonts.googleapis.com/css2?family=Oswald:wght@400;500&family=Open+Sans:wght@400;600;700&family=Montserrat:wght@400;500&family=Arimo:wght@700&display=swap">
<style>
:root{
  --red:#ec1f27;
  --green:#9bcb3c;
  --green-dark:#6f9a27;
  --green-soft:#c6e3a2;
  --white:#ffffff;
  --ink:#222222;
  --text:#3a3a3a;
  --topbar:#f3f7ea;
  --cell:#f8f9f1;
  --line:#dfe6cf;
  --footer:#1d2023;
  --footer-deep:#131517;
  --muted:#9a9ea2;
}
*{box-sizing:border-box;margin:0;padding:0}
html,body{width:1200px;height:3056px;overflow:hidden;background:var(--white)}
body{position:relative;font-family:"Open Sans",Arial,sans-serif;color:var(--text)}
.abs{position:absolute}
.ribbon{width:14px;height:20px;vertical-align:middle}
.section-title{font-family:"Oswald",Arial,sans-serif;font-weight:400;font-size:23px;letter-spacing:4px;color:var(--ink);text-align:center;display:flex;align-items:center;justify-content:center;gap:18px}
.section-title .accent{color:var(--red)}

/* top bar */
.topbar{left:0;top:0;width:1200px;height:62px;background:var(--topbar);border-bottom:1px solid #e3ead3}
.tagline{left:80px;top:22px;font-size:13px;color:#555}
.social-top{right:80px;top:22px;display:flex;gap:26px}
.social-top span{width:14px;height:14px;border-radius:50%;background:#222}
.social-top span.on{background:var(--green)}

/* header */
.header{left:0;top:62px;width:1200px;height:95px;background:var(--white)}
.logo{left:78px;top:22px;font-family:"Montserrat",Arial,sans-serif;font-weight:400;font-size:42px;letter-spacing:9px;color:#1a1a1a}
.phone{right:78px;top:28px;display:flex;align-items:center;gap:14px;font-family:"Montserrat",Arial,sans-serif;font-size:25px;letter-spacing:2px;color:#333}

/* nav */
.nav{left:0;top:157px;width:1200px;height:51px;background:var(--green);display:flex;justify-content:center;gap:46px;padding-left:20px}
.nav a{color:var(--white);text-decoration:none;font-size:14px;line-height:51px;position:relative}
.nav a.current{font-weight:700}
.nav a.current::after{content:"";position:absolute;left:0;right:0;bottom:9px;height:2px;background:var(--white)}

/* hero */
.hero{left:0;top:208px;width:1200px;height:576px;background:linear-gradient(100deg,#7fb7aa 0%,#aac9c6 35%,#c9cfcf 60%,#b8c4cc 100%)}
.hero-title{left:0;top:20px;width:1200px;text-align:center;font-family:"Arimo",Arial,sans-serif;font-weight:700;font-size:54px;letter-spacing:1px;color:#8a9192}
.hexes{left:78px;top:92px}
.hero-dots{left:573px;top:500px;display:flex;gap:8px}
.hero-dots span{width:10px;height:10px;border:1px solid #fff;background:rgba(255,255,255,.3)}
.hero-dots span.on{background:var(--red);border-color:var(--red)}
.chevron{left:0;top:448px}

/* nutrition */
.nutrition{left:0;top:784px;width:1200px;height:238px;background:var(--green-soft)}
.nutrition .section-title{margin-top:44px}
.nutrition p{width:820px;margin:26px auto 0;text-align:center;font-size:14px;line-height:30px;color:#333}

/* diet steps */
.steps-photo{left:0;top:1022px;width:418px;height:380px;background:linear-gradient(120deg,#e9e4dc,#d8c9b8 55%,#a8c27a)}
.steps-head{left:418px;top:1022px;width:782px;height:72px;background:var(--white);padding-top:22px}
.steps-grid{left:418px;top:1094px;width:782px;height:308px}
.step{position:absolute;background:var(--cell);border-right:1px solid var(--line);border-bottom:1px solid var(--line);text-align:center;color:#333}
.step svg{display:block;margin:20px auto 6px}
.step b{display:block;font-size:16px;font-weight:700;color:#222}
.step small{display:block;font-size:16px;margin-top:2px}
.step.active{background:var(--red);color:var(--white)}
.step.active b{color:var(--white)}

/* video band */
.video{left:0;top:1402px;width:1200px;height:313px;background:linear-gradient(90deg,#d94a4b,#e05a58 45%,#d54646)}
.play{left:567px;top:70px}
.video-title{left:0;top:145px;width:1200px;text-align:center;font-family:"Arimo",Arial,sans-serif;font-weight:700;font-size:37px;letter-spacing:1px;color:var(--white)}
.video-rule{left:322px;top:207px;width:558px;height:2px;background:var(--white)}
.video-arrows{left:572px;top:242px}

/* recipes & story */
.recipes{left:0;top:1715px;width:600px;height:418px;background:linear-gradient(135deg,#f3f1ed,#e9ece2)}
.story{left:600px;top:1715px;width:600px;height:418px;background:linear-gradient(135deg,#dfe9c9,#cfe0b3 60%,#c3d6b0)}
.panel-title{position:absolute;top:80px;left:0;width:600px}
.panel-text{position:absolute;top:138px;left:70px;width:460px;text-align:center;font-size:14px;line-height:30.5px;color:#222}
.btn-more{position:absolute;left:210px;top:295px;width:171px;height:50px;background:var(--green-soft);border:2px solid #4f6b2c;font-weight:700;font-size:16px;letter-spacing:.5px;color:#222;line-height:46px;text-align:center}
.story .panel-text{top:140px;line-height:29.5px}
.story-name{position:absolute;left:0;top:246px;width:600px;text-align:center;font-weight:700;font-size:15px;color:#222}
.story-dots{position:absolute;left:257px;top:312px;display:flex;gap:5px}
.story-dots span{width:11px;height:11px;border:1px solid #555}
.story-dots span.on{background:var(--red);border-color:var(--red)}

/* news */
.news{left:0;top:2133px;width:1200px;height:454px;background:var(--white)}
.news .section-title{margin-top:52px}
.news-photo{left:413px;top:118px;width:373px;height:159px;border:3px solid #d6d6d6;background:linear-gradient(90deg,#e8c6cf,#f1d9dc 50%,#e6c0c8)}
.news p{position:absolute;left:250px;top:290px;width:700px;text-align:center;font-size:14px;line-height:25px;color:#222}
.news p a{color:var(--red);text-decoration:none}
.news-arrows{left:572px;top:360px}

/* contact tab */
.contact-tab{left:218px;top:2587px;width:764px;height:102px;display:flex;z-index:2}
.contact-tab div{flex:1;display:flex;align-items:center;gap:24px;color:var(--white);font-size:20px}
.tab-phone{background:var(--green)}
.tab-mail{background:var(--green-dark)}
.tab-icon{width:46px;height:102px;display:flex;align-items:center;justify-content:center;background:rgba(0,0,0,.12)}
.fold{top:2587px;z-index:1}

/* footer */
.footer{left:0;top:2638px;width:1200px;height:367px;background:var(--footer)}
.footer-logo{left:106px;top:88px;font-family:"Montserrat",Arial,sans-serif;font-size:34px;letter-spacing:8px;color:#b9bcbf}
.footer-text{left:90px;top:164px;width:290px;text-align:center;font-size:14px;line-height:23px;color:#e6e6e6}
.social-foot{left:150px;top:232px;display:flex;gap:14px}
.social-foot span{width:30px;height:30px;border:1px solid #8d9195}
.social-foot span.on{background:var(--green);border-color:var(--green)}
.touch-title{left:493px;top:92px;width:628px;font-family:"Oswald",Arial,sans-serif;font-size:21px;letter-spacing:3px;color:var(--green);display:flex;justify-content:center;align-items:center;gap:14px}
.touch-title .accent{color:var(--red)}
.field{position:absolute;height:29px;border:1px solid #3a3e42;background:#181b1d;font-size:10px;color:#6d7175;padding:8px 10px;letter-spacing:.5px}
.send{left:493px;top:291px;width:628px;height:29px;background:var(--green);color:#1b1b1b;font-weight:700;font-size:12px;letter-spacing:1px;text-align:center;line-height:29px}
.copyright{left:0;top:3005px;width:1200px;height:51px;background:var(--footer-deep);text-align:center;line-height:51px;font-size:11px;color:#8f9397}
.copyright b{color:var(--green);font-weight:600}
</style>
</head>
<body>

<svg width="0" height="0" style="position:absolute">
  <defs>
    <symbol id="ribbon" viewBox="0 0 14 20">
      <path d="M7 2c-2.3 0-3.6 1.6-3.2 3.8.3 1.6 1.3 3 2.2 4.2L1.5 18l2 1.5L7 12.8l3.5 6.7 2-1.5L8 10c.9-1.2 1.9-2.6 2.2-4.2C10.6 3.6 9.3 2 7 2zm0 2.2c.9 0 1.4.7 1.2 1.6-.2.9-.7 1.8-1.2 2.6-.5-.8-1-1.7-1.2-2.6C5.6 4.9 6.1 4.2 7 4.2z" fill="#111"/>
    </symbol>
  </defs>
</svg>

<!-- Top bar -->
<div class="abs topbar">
  <div class="abs tagline">The Science Behind What We Eat</div>
  <div class="abs social-top"><span></span><span class="on"></span><span></span><span></span></div>
</div>

<!-- Header -->
<header class="abs header">
  <div class="abs logo">VITA PLATE</div>
  <div class="abs phone">
    <svg width="30" height="30" viewBox="0 0 24 24"><path d="M6.6 10.8c1.4 2.8 3.8 5.1 6.6 6.6l2.2-2.2c.3-.3.7-.4 1-.2 1.1.4 2.3.6 3.6.6.6 0 1 .4 1 1V20c0 .6-.4 1-1 1C10.6 21 3 13.4 3 4c0-.6.4-1 1-1h3.5c.6 0 1 .4 1 1 0 1.3.2 2.5.6 3.6.1.3 0 .7-.2 1L6.6 10.8z" fill="#8b8f93"/></svg>
    <span>+48 600 412 097</span>
  </div>
</header>

<!-- Navigation -->
<nav class="abs nav">
  <a class="current" href="#">Home</a>
  <a href="#">Diet Steps</a>
  <a href="#">FernaMeal Videos</a>
  <a href="#">Cancer News</a>
  <a href="#">Team</a>
  <a href="#">Testimonial</a>
  <a href="#">Blog</a>
  <a href="#">Contact Us</a>
</nav>

<!-- Hero -->
<section class="abs hero" role="img" aria-label="Hero photo: a patient in a head scarf resting in a hospital bed with a caregiver beside her">
  <div class="abs hero-title">YOU ARE WHAT YOU EAT</div>
  <svg class="abs hexes" width="390" height="320" viewBox="0 0 390 320">
    <g stroke="#fff" stroke-width="3">
      <polygon points="77,6 150,48 150,132 77,174 4,132 4,48" fill="#3fa7a7" role="img" aria-label="Photo of a smiling nurse"/>
      <polygon points="233,6 306,48 306,132 233,174 160,132 160,48" fill="#77b56a" role="img" aria-label="Photo of a woman eating a salad"/>
      <polygon points="155,140 228,182 228,266 155,308 82,266 82,182" fill="#4f7a96" role="img" aria-label="Photo of fresh green vegetables"/>
      <polygon points="311,140 384,182 384,266 311,308 238,266 238,182" fill="#c98f97" role="img" aria-label="Photo of hands joined around a pink ribbon"/>
    </g>
  </svg>
  <div class="abs hero-dots"><span></span><span class="on"></span><span></span></div>
  <svg class="abs chevron" width="1200" height="128" viewBox="0 0 1200 128">
    <polygon points="0,0 600,128 1200,0 1200,128 0,128" fill="#c6e3a2"/>
    <polyline points="0,0 600,128 1200,0" fill="none" stroke="#5f8f1c" stroke-width="8"/>
    <polyline points="0,10 600,138 1200,10" fill="none" stroke="#8fc040" stroke-width="8"/>
  </svg>
</section>

<!-- Nutrition diagnostics -->
<section class="abs nutrition">
  <h2 class="section-title"><svg class="ribbon"><use href="#ribbon"/></svg><span>NUTRITION <span class="accent">DIAGNOSTICS</span></span><svg class="ribbon"><use href="#ribbon"/></svg></h2>
  <p>Lorem ipsum dolor sit amet, consectetur adipiscing elit, sed do eiusmod tempor incididunt ut labore et dolore magna aliqua. Ut enim ad minim veniam, quis nostrud exercitation ullamco laboris nisi ut aliquip ex ea commodo consequat. Duis aute irure dolor in reprehenderit in voluptate velit esse cillum dolore eu fugiat nulla pariatur.</p>
</section>

<!-- Diet steps -->
<div class="abs steps-photo" role="img" aria-label="Photo of a smiling woman holding a grocery bag of fresh vegetables"></div>
<div class="abs steps-head">
  <h2 class="section-title"><svg class="ribbon"><use href="#ribbon"/></svg><span>DIET <span class="accent">STEPS</span></span><svg class="ribbon"><use href="#ribbon"/></svg></h2>
</div>
<div class="abs steps-grid">
  <div class="step active" style="left:0;top:0;width:261px;height:153px">
    <svg width="44" height="44" viewBox="0 0 44 44" fill="none" stroke="#fff" stroke-width="2.5"><circle cx="22" cy="22" r="18"/><circle cx="22" cy="22" r="9"/><path d="M4 22h36M22 4v36"/></svg>
    <b>STEP 1 :</b><small>Prevention of oncological</small>
  </div>
  <div class="step" style="left:261px;top:0;width:261px;height:153px">
    <svg width="44" height="44" viewBox="0 0 44 44" fill="none" stroke="#222" stroke-width="2.5"><circle cx="22" cy="14" r="8"/><circle cx="13" cy="29" r="8"/><circle cx="31" cy="29" r="8"/><circle cx="22" cy="24" r="3" fill="#222"/></svg>
    <b>STEP 2 :</b><small>Diet chemotherapy</small>
  </div>
  <div class="step" style="left:522px;top:0;width:260px;height:153px">
    <svg width="44" height="44" viewBox="0 0 44 44" fill="none" stroke="#222" stroke-width="2.5"><path d="M10 6h16v8H10zM18 14v12M8 38h28M12 38v-6h20v6M26 26h8"/></svg>
    <b>STEP 3 :</b><small>Diet in Radiotherapy</small>
  </div>
  <div class="step" style="left:0;top:153px;width:391px;height:155px">
    <svg width="44" height="44" viewBox="0 0 44 44" fill="none" stroke="#222" stroke-width="2.5"><circle cx="26" cy="16" r="7"/><path d="M26 23v14M20 31h12M12 10l-4 4M6 18h4M14 6v4"/></svg>
    <b>STEP 4 :</b><small>Hormonal Diet</small>
  </div>
  <div class="step" style="left:391px;top:153px;width:391px;height:155px">
    <svg width="44" height="44" viewBox="0 0 44 44" fill="none" stroke="#222" stroke-width="2.5"><circle cx="22" cy="24" r="15"/><path d="M18 5h8M22 5v4M16 24l6 6 8-10"/></svg>
    <b>STEP 5 :</b><small>Diet During convalescence</small>
  </div>
</div>

<!-- Video band -->
<section class="abs video" role="img" aria-label="Video still: a woman preparing food in a kitchen, tinted red">
  <svg class="abs play" width="66" height="66" viewBox="0 0 66 66"><circle cx="33" cy="33" r="30" fill="none" stroke="#fff" stroke-width="4"/><circle cx="33" cy="33" r="22" fill="#fff"/><polygon points="27,21 45,33 27,45" fill="#e05a58"/></svg>
  <div class="abs video-title">Anti Vita Plate Flush</div>
  <div class="abs video-rule"></div>
  <svg class="abs video-arrows" width="56" height="22" viewBox="0 0 56 22" fill="#fff"><polygon points="0,11 12,2 12,7 22,7 22,15 12,15 12,20"/><polygon points="56,11 44,2 44,7 34,7 34,15 44,15 44,20"/></svg>
</section>

<!-- Recipes -->
<section class="abs recipes" role="img" aria-label="Faded photo of fresh ingredients on a kitchen table">
  <h2 class="section-title panel-title"><svg class="ribbon"><use href="#ribbon"/></svg><span>VITA PLATE <span class="accent">RECIPES</span></span><svg class="ribbon"><use href="#ribbon"/></svg></h2>
  <p class="panel-text">At VitaPlate.com we are diving into the science and chemistry of what we eat and how it effects our bodies in ways we could not imagine until recently. It is true - you are what you eat, and we intend to show you how you can eat your way to a healthy and cancer free life.</p>
  <div class="btn-more">READ MORE</div>
</section>

<!-- Success story -->
<section class="abs story" role="img" aria-label="Faded photo of a doctor comforting an older patient">
  <h2 class="section-title panel-title"><svg class="ribbon"><use href="#ribbon"/></svg><span>OUR SUCCESS <span class="accent">STORY</span></span><svg class="ribbon"><use href="#ribbon"/></svg></h2>
  <p class="panel-text">Lorem ipsum dolor sit amet, consectetur adipiscing elit, sed do eiusmod tempor incididunt ut labore et dolore magna aliqua. Ut enim ad minim veniam.</p>
  <div class="story-name">-NAME HERE</div>
  <div class="story-dots"><span></span><span class="on"></span><span></span><span></span><span></span><span></span></div>
</section>

<!-- Cancer news -->
<section class="abs news">
  <h2 class="section-title"><svg class="ribbon"><use href="#ribbon"/></svg><span>CANCER <span class="accent">NEWS</span></span><svg class="ribbon"><use href="#ribbon"/></svg></h2>
  <div class="abs news-photo" role="img" aria-label="Photo of five women in pink shirts standing together"></div>
  <p>Lorem ipsum dolor sit amet, consectetur adipiscing elit, sed do eiusmod tempor incididunt ut labore et dolore magna aliqua. Ut enim ad minim......<a href="#">READ MORE</a></p>
  <svg class="abs news-arrows" width="56" height="22" viewBox="0 0 56 22"><polygon points="0,11 12,2 12,7 22,7 22,15 12,15 12,20" fill="#222"/><polygon points="56,11 44,2 44,7 34,7 34,15 44,15 44,20" fill="#9bcb3c"/></svg>
</section>

<!-- Contact tab -->
<svg class="abs fold" style="left:198px" width="20" height="51" viewBox="0 0 20 51"><polygon points="20,0 20,51 0,51" fill="#7fa531"/></svg>
<svg class="abs fold" style="left:982px" width="20" height="51" viewBox="0 0 20 51"><polygon points="0,0 0,51 20,51" fill="#557a1a"/></svg>
<div class="abs contact-tab">
  <div class="tab-phone">
    <span class="tab-icon"><svg width="22" height="22" viewBox="0 0 24 24"><path d="M6.6 10.8c1.4 2.8 3.8 5.1 6.6 6.6l2.2-2.2c.3-.3.7-.4 1-.2 1.1.4 2.3.6 3.6.6.6 0 1 .4 1 1V20c0 .6-.4 1-1 1C10.6 21 3 13.4 3 4c0-.6.4-1 1-1h3.5c.6 0 1 .4 1 1 0 1.3.2 2.5.6 3.6.1.3 0 .7-.2 1L6.6 10.8z" fill="#fff"/></svg></span>
    <span>+48 600 412 097</span>
  </div>
  <div class="tab-mail">
    <span class="tab-icon"><svg width="22" height="22" viewBox="0 0 24 24" fill="none" stroke="#fff" stroke-width="2.4"><path d="M10 14a4 4 0 0 0 5.7 0l4-4a4 4 0 0 0-5.7-5.7l-1.5 1.5"/><path d="M14 10a4 4 0 0 0-5.7 0l-4 4a4 4 0 0 0 5.7 5.7l1.5-1.5"/></svg></span>
    <span>info@vitaplate.com</span>
  </div>
</div>

<!-- Footer -->
<footer class="abs footer">
  <div class="abs footer-logo">VITA PLATE</div>
  <p class="abs footer-text">Please feel free to call or email for general questions, order status &amp; press inquiries.</p>
  <div class="abs social-foot"><span></span><span class="on"></span><span></span><span></span></div>

  <h2 class="abs touch-title"><svg class="ribbon"><use href="#ribbon" style="fill:#fff"/></svg><span>KEEP IN <span class="accent">TOUCH</span></span><svg class="ribbon"><use href="#ribbon"/></svg></h2>
  <div class="field" style="left:493px;top:145px;width:310px">NAME</div>
  <div class="field" style="left:813px;top:145px;width:308px">EMAIL ID</div>
  <div class="field" style="left:493px;top:179px;width:628px;height:106px">MESSAGE</div>
  <div class="abs send">SEND</div>
</footer>
<div class="abs copyright"><b>© VITA PLATE</b> - 2015. All Rights are reserved.</div>

</body>
</html>
```